"Recently Leased" flyer for real estate agency

Looking to have a Recently Leased flyer designed. This will be delivered to apartments and houses closely situated to a property we have recently leased. The idea is to get the attention of owner/landlords in the area that may be considering leasing their property in the future and inform them of the great work we are doing locally. I would like the design to be a two sided flyer using the photoshop (PSD) template below (we would like to be able to edit this once complete should we need to update copy etc in the future). I would like the front page to look like our "for lease sign with the leased sticker on it and copy, I dont want it to look like a typical junk mail flyer.

Target Market(s)

Property owners and investors, male and female aged 28-70

Industry/Entity Type

Real Estate

Font styles to use
Sans Serif

Colors

Designer to choose colors to be used in the design.

Requirements
Must have
• Harbor Keystone Logo
• Contact information
• Copy supplied
Nice to have
• Slick, clean design,
Should not have
• too many colours or too busy a design.
• NO PROPERTY PHOTOS ON FRONT - I want this to be generic and not relate to a specific property image which might confuse people.

```html
<!DOCTYPE html>
<html lang="en">
<head>
<meta charset="utf-8">
<title>Harbor Keystone – Leased Flyer</title>
<link rel="stylesheet" href="https://fonts.googleapis.com/css2?family=Lato:wght@300;400;700&display=swap">
<style>
  :root{
    --stage:#d3d3d5;
    --navy:#2f5079;
    --navy-deep:#2b4a72;
    --sea-light:#6f9cc4;
    --red:#c3292e;
    --red-sticker:#b1343a;
    --tick:#d8282f;
    --white:#ffffff;
    --rule:#6b86a8;
  }
  *{box-sizing:border-box;margin:0;padding:0}
  html,body{width:1022px;height:1200px;overflow:hidden}
  body{background:var(--stage);font-family:"Lato",sans-serif;color:var(--white);position:relative}
  .side{position:absolute;top:185px;width:382px;height:831px;background:var(--navy);overflow:hidden}
  .side--front{left:95px}
  .side--back{left:514px;background:linear-gradient(to bottom,var(--navy) 0,var(--navy) 560px,var(--navy-deep) 600px,var(--sea-light) 690px,var(--sea-light) 831px)}
  .brand{position:absolute;left:0;right:0;text-align:center;font-weight:700;font-size:30px;letter-spacing:.5px;line-height:1}
  .brand__sub{display:block;font-size:10px;letter-spacing:1px;margin-top:6px}
  .side--front .brand{top:82px}
  .side--back .brand{top:75px}
  .sticker{position:absolute;left:29px;top:191px;width:326px;height:77px;background:var(--red-sticker);padding:6px}
  .sticker__frame{width:100%;height:100%;border:2px solid var(--white);display:flex;align-items:center;justify-content:center;font-weight:400;font-size:62px;letter-spacing:1px;line-height:1}
  .copy{position:absolute;left:40px;width:304px;font-size:11.6px;line-height:14.8px;font-weight:400}
  .copy p+p{margin-top:6px}
  .justify{text-align:justify}
  .ticks{position:absolute;left:65px;width:270px;list-style:none;font-size:11.6px;line-height:14.8px}
  .ticks li{position:relative;padding-left:20px;margin-bottom:5.5px}
  .ticks svg{position:absolute;left:0;top:2px;width:9px;height:9px}
  .contact-name{position:absolute;left:0;right:0;text-align:center;font-weight:700;font-size:17px}
  .agency-name{position:absolute;left:0;right:0;text-align:center;font-weight:700;font-size:13px}
  .agency-address{position:absolute;left:0;right:0;text-align:center;font-size:10.5px}
  .rule{position:absolute;left:131px;width:120px;height:1px;background:var(--rule)}
  .pin{position:absolute;left:184px;width:14px;height:14px}
  .coast{position:absolute;left:0;right:0;top:671px;height:105px;background:linear-gradient(to bottom,#8a9a86 0,#6c8a6e 22%,#c9c2ad 35%,#3f7fa6 55%,#5fa4c6 75%,#9ccde0 100%)}
  .footer{position:absolute;left:0;right:0;bottom:0;height:55px;background:var(--red);display:flex;flex-direction:column;align-items:center;justify-content:center;font-size:13.4px;line-height:18px;letter-spacing:.4px}
</style>
</head>
<body>
<svg width="0" height="0" style="position:absolute">
  <symbol id="tick" viewBox="0 0 10 10">
    <circle cx="5" cy="5" r="5" fill="#d8282f"/>
    <path d="M2.6 5.1 L4.4 6.8 L7.5 3.4" fill="none" stroke="#fff" stroke-width="1.5" stroke-linecap="round" stroke-linejoin="round"/>
  </symbol>
</svg>

<section class="side side--front">
  <div class="brand">HARBOR KEYSTONE<span class="brand__sub">AGENCY</span></div>
  <div class="sticker"><div class="sticker__frame">LEASED!</div></div>

  <div class="copy justify" style="top:284px">
    <p>We recently leased a property in your building or street. Attracting a great reliable tenant and fantastic return for the owner.</p>
    <p>We received a high number of enquires and applications for this property and have a database of screened and qualified tenants looking to lease in your area.</p>
  </div>

  <ul class="ticks" style="top:395px">
    <li><svg><use href="#tick"/></svg>On average we lease properties 2 weeks faster than the Northern Beaches average</li>
    <li><svg><use href="#tick"/></svg>Strong database of tenants actively looking in the area</li>
    <li><svg><use href="#tick"/></svg>All we do is lease property, no sales – so tenanting and managing your property is our priority</li>
    <li><svg><use href="#tick"/></svg>90 day money back guarantee on our level of service</li>
    <li><svg><use href="#tick"/></svg>Highly competitive, simple all-inclusive pricing.</li>
    <li><svg><use href="#tick"/></svg>Experience the difference of a property management specialist</li>
  </ul>

  <div class="copy" style="top:632px">
    <p>Contact <strong>Sam</strong> to get your free rental appraisal or transfer your existing investment to an agency that will give it the attention it deserves and maxamise your return.</p>
  </div>

  <div class="contact-name" style="top:690px">Sam Carver&nbsp; 0400 555 217</div>
  <div class="rule" style="top:717px"></div>
  <div class="agency-name" style="top:728px">Harbor Keystone Agency</div>
  <div class="agency-address" style="top:747px">Level 1, 12 Marlow Rd, Fairhaven NSW 2099</div>

  <div class="footer">
    <span>sam@harborkeystoneagency.com.au</span>
    <span>www.harborkeystoneagency.com.au</span>
  </div>
</section>

<section class="side side--back">
  <div class="brand">HARBOR KEYSTONE<span class="brand__sub">AGENCY</span></div>

  <div class="copy justify" style="top:176px">
    <p>The fundamental idea behind Harbor Keystone Agency was to give landlords a simple and confidence inspiring experience. We achieve this through:</p>
  </div>

  <ul class="ticks" style="top:232px;width:280px">
    <li><svg><use href="#tick"/></svg>Unique marketing that goes beyond the standard listing sites and has seen our average days-on-market at 5.9days for 2018.</li>
    <li><svg><use href="#tick"/></svg>A simple, yet competitive fee structure.</li>
    <li><svg><use href="#tick"/></svg>Excellent customer service through an experienced professional property manager.</li>
    <li><svg><use href="#tick"/></svg>Sound advice and communication through out the leasing and management process.</li>
    <li><svg><use href="#tick"/></svg>A simple yet powerful landlord portal which enables owners to view media rich inspection reports, financial reports and maintenance progress at anytime.</li>
    <li><svg><use href="#tick"/></svg>We then back our service promise with a 90day money back guarantee.</li>
  </ul>

  <div class="copy justify" style="top:482px">
    <p>If you have been considering leasing your property, purchasing a local investment or aren't happy with your current managing agency, please don't hesitate to contact your local rental specialist for more information:</p>
  </div>

  <div class="contact-name" style="top:568px">Sam Carver&nbsp; 0400 555 217</div>
  <div class="rule" style="top:597px"></div>
  <svg class="pin" style="top:609px" viewBox="0 0 14 14" aria-hidden="true">
    <circle cx="7" cy="7" r="6.5" fill="#fff"/>
    <path d="M7 3.2a2.4 2.4 0 0 0-2.4 2.4c0 1.8 2.4 4.6 2.4 4.6s2.4-2.8 2.4-4.6A2.4 2.4 0 0 0 7 3.2z" fill="var(--navy)"/>
    <circle cx="7" cy="5.6" r=".9" fill="#fff"/>
  </svg>
  <div class="agency-name" style="top:630px">Harbor Keystone Agency</div>
  <div class="agency-address" style="top:649px">Level 1, 12 Marlow Rd, Fairhaven NSW 2099</div>

  <div class="coast" role="img" aria-label="Coastal scene: beachside suburb on a headland above a sandy beach and breaking turquoise surf"></div>

  <div class="footer">
    <span>sam@harborkeystoneagency.com.au</span>
    <span>www.harborkeystoneagency.com.au</span>
  </div>
</section>
</body>
</html>
```